Business Card Design Project

Cyber Security. Company name is brightHarbor.

Industry/Entity Type

Computer Security

Contact Information for Business Card

Gregory Lindqvist
Founder and Chief Hacker

2370 W. Alder Rd.
Suite 514
Chicago, IL 60482
773.555.0196
gregory.lindqvist@brightharbor.example
www.brightharbor.example

```html
<!DOCTYPE html>
<html lang="en">
<head>
<meta charset="utf-8">
<title>brightHarbor business card</title>
<link rel="stylesheet" href="https://fonts.googleapis.com/css2?family=Open+Sans:wght@400;600;700&display=swap">
<style>
  :root {
    --backdrop: #4a4848;
    --card-white: #ffffff;
    --card-dark: #2f2b2a;
    --ink: #1c1c1c;
    --ink-soft: #333333;
    --accent-blue: #4a6cc4;
    --rule: #b8b8b8;
    --bar-green: #8cc63f;
    --bar-orange: #f7901e;
    --bar-gray: #a7a9ac;
    --bar-blue: #1c8fd8;
    --mark: #1c8fd8;
    --url-light: #d8d8d8;
  }
  * { margin: 0; padding: 0; box-sizing: border-box; }
  html, body { width: 1200px; height: 896px; overflow: hidden; }
  body {
    background: var(--backdrop);
    font-family: "Open Sans", Arial, sans-serif;
    position: relative;
  }
  .card {
    position: absolute;
    left: 260px;
    width: 680px;
    height: 388px;
    border-radius: 22px;
    overflow: hidden;
  }
  .card--front { top: 40px; background: var(--card-white); color: var(--ink); }
  .card--back { top: 468px; background: var(--card-dark); }

  .brand {
    position: absolute;
    right: 48px;
    top: 44px;
    display: flex;
    align-items: center;
    gap: 14px;
  }
  .brand__dot {
    width: 40px; height: 40px; border-radius: 50%;
    background: var(--mark);
    flex: none;
  }
  .brand__name {
    font-size: 46px;
    line-height: 64px;
    font-weight: 400;
    color: var(--ink);
    letter-spacing: 0.5px;
    white-space: nowrap;
  }

  .person { position: absolute; left: 40px; top: 140px; }
  .person__name {
    font-size: 21px; line-height: 29px; font-weight: 700; text-transform: uppercase;
    letter-spacing: 0.5px; color: var(--ink);
  }
  .person__name .surname { color: var(--accent-blue); }
  .person__title { font-size: 17px; line-height: 24px; color: var(--ink-soft); }

  .contact { position: absolute; left: 40px; top: 206px; list-style: none; }
  .contact li {
    display: flex; align-items: center; gap: 10px;
    font-size: 16px; line-height: 24px; color: var(--ink-soft);
  }
  .contact svg { width: 14px; height: 14px; fill: var(--accent-blue); flex: none; }

  .divider {
    position: absolute; left: 40px; right: 40px; top: 288px;
    height: 1px; background: var(--rule);
  }
  .address {
    position: absolute; right: 40px; top: 296px;
    text-align: right; font-style: normal;
    font-size: 16px; line-height: 21px; color: var(--ink-soft);
  }

  .color-bar {
    position: absolute; left: 0; right: 0; bottom: 0; height: 18px;
    display: flex;
  }
  .color-bar span { height: 100%; }
  .color-bar .green { width: 24%; background: var(--bar-green); }
  .color-bar .orange { width: 25%; background: var(--bar-orange); }
  .color-bar .gray { width: 22%; background: var(--bar-gray); }
  .color-bar .blue { width: 29%; background: var(--bar-blue); }

  .back__mark {
    position: absolute; left: 50%; top: 86px;
    width: 140px; height: 140px; margin-left: -70px;
    border-radius: 50%; background: var(--mark);
  }
  .back__url {
    position: absolute; left: 0; right: 0; top: 268px;
    text-align: center; font-size: 18px; letter-spacing: 2px;
    color: var(--url-light);
  }
</style>
</head>
<body>

<section class="card card--front" aria-label="Card front">
  <div class="brand">
    <span class="brand__dot"></span>
    <span class="brand__name">brightHarbor</span>
  </div>

  <div class="person">
    <p class="person__name">Gregory <span class="surname">Lindqvist</span></p>
    <p class="person__title">Founder and Chief Hacker</p>
  </div>

  <ul class="contact">
    <li>
      <svg viewBox="0 0 16 16" aria-hidden="true"><path d="M3 1h3l1.5 4-2 1.3a8 8 0 0 0 4.2 4.2L11 8.5l4 1.5v3a2 2 0 0 1-2 2A12 12 0 0 1 1 3a2 2 0 0 1 2-2z"/></svg>
      773.555.0196
    </li>
    <li>
      <svg viewBox="0 0 16 16" aria-hidden="true"><path d="M1 3h14v10H1z M1 3l7 6 7-6" stroke="#fff" stroke-width="1.2"/></svg>
      gregory.lindqvist@brightharbor.example
    </li>
    <li>
      <svg viewBox="0 0 16 16" aria-hidden="true"><circle cx="8" cy="8" r="7"/></svg>
      www.brightharbor.example
    </li>
  </ul>

  <div class="divider"></div>

  <address class="address">
    2370 W. Alder Rd.<br>Suite 514<br>Chicago, IL 60482
  </address>

  <div class="color-bar" aria-hidden="true">
    <span class="green"></span><span class="orange"></span><span class="gray"></span><span class="blue"></span>
  </div>
</section>

<section class="card card--back" aria-label="Card back">
  <div class="back__mark"></div>
  <p class="back__url">www.brightharbor.example</p>
</section>

</body>
</html>
```